Creative Business Card

Were looking for a new fresh and creative look to our Business card. Our company name is InkVale. Be creative, Were attaching our logo and our base colors, but your free to do anything. Name, title, Phone

Industry/Entity Type

Business

```html
<!DOCTYPE html>
<html lang="en">
<head>
<meta charset="utf-8">
<title>InkVale Business Card</title>
<link rel="stylesheet" href="https://fonts.googleapis.com/css2?family=Open+Sans:wght@400;600;800&display=swap">
<style>
  :root {
    --stage: #eceae6;
    --green-dark: #2f5a1c;
    --green-mid: #4f8a2c;
    --green-light: #7dbb42;
    --brand-green: #7cc242;
    --ink-blue: #1f6fb8;
    --title-blue: #2b5f8f;
    --card-white: #ffffff;
    --shadow: rgba(0, 0, 0, 0.18);
  }
  * { box-sizing: border-box; margin: 0; padding: 0; }
  html, body {
    width: 1200px;
    height: 784px;
    overflow: hidden;
    background: var(--stage);
    font-family: "Open Sans", Arial, sans-serif;
  }
  .card-set {
    position: relative;
    width: 1200px;
    height: 784px;
  }
  .card {
    position: absolute;
    top: 238px;
    width: 540px;
    height: 308px;
    border-radius: 4px;
    overflow: hidden;
    box-shadow: 0 10px 28px var(--shadow);
  }
  .card-front { left: 40px; }
  .card-back { left: 620px; background: var(--card-white); }

  .front-pattern {
    position: absolute;
    inset: 0;
    background:
      radial-gradient(ellipse at 30% 70%, var(--green-light) 0%, var(--green-mid) 45%, var(--green-dark) 100%);
  }
  .front-wordmark {
    position: absolute;
    left: 0; right: 0;
    top: 112px;
    text-align: center;
    font-weight: 800;
    font-size: 64px;
    letter-spacing: 1px;
    color: var(--card-white);
    line-height: 1;
  }

  .back-wordmark {
    position: absolute;
    left: 40px;
    top: 54px;
    font-weight: 800;
    font-size: 58px;
    letter-spacing: 1px;
    color: var(--brand-green);
    line-height: 1;
  }
  .holder {
    position: absolute;
    left: 40px;
    top: 168px;
  }
  .holder-name {
    font-weight: 600;
    font-size: 19px;
    color: var(--brand-green);
    line-height: 1.1;
  }
  .holder-title {
    font-size: 12px;
    color: var(--title-blue);
    margin-top: 2px;
  }
  .contact-list {
    list-style: none;
    position: absolute;
    left: 40px;
    top: 218px;
  }
  .contact-item {
    display: flex;
    align-items: center;
    gap: 8px;
    font-size: 15px;
    line-height: 20px;
    color: var(--ink-blue);
  }
  .contact-icon { width: 15px; height: 15px; flex: none; }
</style>
</head>
<body>
  <main class="card-set">
    <section class="card card-front">
      <div class="front-pattern" role="img" aria-label="Green background with a pattern of soft overlapping circles"></div>
      <div class="front-wordmark">INKVALE</div>
    </section>

    <section class="card card-back">
      <div class="back-wordmark">INKVALE</div>
      <div class="holder">
        <div class="holder-name">Dana Hollis</div>
        <div class="holder-title">Manager</div>
      </div>
      <ul class="contact-list">
        <li class="contact-item">
          <svg class="contact-icon" viewBox="0 0 16 16" aria-hidden="true"><path fill="#7cc242" d="M3.5 1.5l2.3 2.6-1.3 1.8c.9 2 2.6 3.7 4.6 4.6l1.8-1.3 2.6 2.3-1.4 2.2C6.6 13.5 2.5 9.4 1.3 3.9z"/></svg>
          <span>(555) 214-0386</span>
        </li>
        <li class="contact-item">
          <svg class="contact-icon" viewBox="0 0 16 16" aria-hidden="true"><rect x="1" y="3.5" width="14" height="10" rx="1" fill="#7cc242"/><path d="M1.5 4.5l6.5 5 6.5-5" fill="none" stroke="#fff" stroke-width="1.3"/></svg>
          <span>dana@inkvale.com</span>
        </li>
        <li class="contact-item">
          <svg class="contact-icon" viewBox="0 0 16 16" aria-hidden="true"><circle cx="8" cy="8" r="6.5" fill="none" stroke="#7cc242" stroke-width="1.5"/><ellipse cx="8" cy="8" rx="2.8" ry="6.5" fill="none" stroke="#7cc242" stroke-width="1.2"/><path d="M1.5 8h13M2.6 4.7h10.8M2.6 11.3h10.8" stroke="#7cc242" stroke-width="1.1"/></svg>
          <span>www.inkvale.com</span>
        </li>
        <li class="contact-item">
          <svg class="contact-icon" viewBox="0 0 16 16" aria-hidden="true"><path fill="#7cc242" d="M8 1.5L.8 8h2.2v6.5h3.8v-4h2.4v4h3.8V8h2.2z"/></svg>
          <span>412 Cedar Hollow Road, Suite B</span>
        </li>
      </ul>
    </section>
  </main>
</body>
</html>
```